Business Card Design Project - IT Company

CLOUD IT company working with medium to large corporate clients requires 2 sided Business Card design.

Strong, Professional and modern is what I am looking for.

The Logo JPG attached has all the colour palette options. which consist of Red and Silver on various backgrounds

Preferred option for the Back of card is either Silver Text on Red or Silver Text on Black. Though this is not concrete. Surprise me.

Logo must be prominent along with Contact details of the staff member

Tagline can be all Capitals " CLOUD MANAGED SERVICES"

I will look to provide feedback and tweaks to get the right design so it should be a fun process.

I will provide the layered files to the top few contenders.

Reason: Leaving the door open for some creativity. Don't forget this is an technology company. .

Target Market(s)

Leaders, decision makers, CEOs, CIOs,

Industry/Entity Type

Business

Requirements
Must have
• Data must have is

Company Name: Velquora
Tagline: Cloud Managed Services

No Particular order

First Name Last name
Director
Mobile 0452 987 654
www.velquora.com
First.Lastname@velquora.com
Suite 5, 48 Marlowe Lane, Sydney NSW 2000

```html
<!DOCTYPE html>
<html lang="en">
<head>
<meta charset="utf-8">
<title>Velquora Business Card</title>
<link href="https://fonts.googleapis.com/css2?family=Quicksand:wght@400;500;700&display=swap" rel="stylesheet">
<style>
  :root {
    --backdrop: #3a302b;
    --card-white: #f4f4f4;
    --card-black: #1c1c1d;
    --brand-red: #c8202a;
    --band-grey: #c9c9c9;
    --dark-grey: #5a5a5c;
    --ink: #2a2a2a;
    --soft-ink: #8a8a8a;
    --silver: #b9bbbe;
  }
  * { margin: 0; padding: 0; box-sizing: border-box; }
  html, body { width: 1200px; height: 832px; overflow: hidden; }
  body {
    background: var(--backdrop);
    font-family: "Quicksand", sans-serif;
    position: relative;
  }
  .card {
    position: absolute;
    top: 261px;
    width: 540px;
    height: 310px;
    overflow: hidden;
    box-shadow: 0 10px 30px rgba(0,0,0,.45);
  }
  .card-front { left: 40px; background: var(--card-white); }
  .card-back { left: 620px; background: var(--card-black); }

  /* front */
  .front-band {
    position: absolute; top: 0; right: 0;
    width: 150px; height: 22px; background: var(--band-grey);
  }
  .front-accent {
    position: absolute; right: 0; top: 212px;
    width: 22px; height: 40px; background: var(--brand-red);
  }
  .brand {
    position: absolute; display: flex; align-items: center; gap: 10px;
  }
  .brand-front { top: 48px; right: 46px; }
  .brand-mark {
    width: 34px; height: 34px; border-radius: 50%;
    background: var(--brand-red);
  }
  .brand-text { display: flex; flex-direction: column; align-items: flex-end; }
  .brand-name {
    font-weight: 700; font-size: 44px; line-height: 1; color: var(--ink);
    letter-spacing: -0.5px;
  }
  .brand-tagline {
    font-weight: 700; font-size: 10px; letter-spacing: 0.6px;
    color: var(--ink); margin-top: 2px;
  }
  .staff {
    position: absolute; left: 48px; top: 58px; color: var(--soft-ink);
  }
  .staff-name { font-size: 17px; font-weight: 500; letter-spacing: 0.5px; }
  .staff-role { font-size: 11px; margin-top: 4px; }
  .contact-list { list-style: none; margin-top: 16px; font-size: 13px; }
  .contact-list li { display: flex; gap: 8px; line-height: 1.55; }
  .contact-label { color: var(--brand-red); font-weight: 700; width: 10px; }
  .company-info {
    position: absolute; right: 48px; top: 168px; text-align: right;
    color: var(--dark-grey); font-size: 13px; line-height: 1.55;
  }
  .web { color: var(--ink); margin-bottom: 22px; font-size: 13px; }
  .web strong { color: var(--brand-red); font-weight: 700; }

  /* back */
  .back-band-red {
    position: absolute; top: 0; right: 0;
    width: 150px; height: 14px; background: var(--brand-red);
  }
  .back-band-grey {
    position: absolute; top: 14px; right: 0;
    width: 95px; height: 26px; background: var(--dark-grey);
  }
  .back-edge {
    position: absolute; left: 0; top: 40px;
    width: 22px; height: 12px; background: var(--dark-grey);
  }
  .brand-back {
    left: 50%; top: 50%; transform: translate(-50%, -50%);
  }
  .brand-back .brand-mark { background: var(--silver); width: 40px; height: 40px; }
  .brand-back .brand-name { color: var(--silver); font-size: 52px; }
  .brand-back .brand-tagline { color: var(--silver); font-size: 11px; }
</style>
</head>
<body>
  <section class="card card-front" aria-label="Card front">
    <div class="front-band"></div>
    <div class="front-accent"></div>

    <div class="staff">
      <p class="staff-name">MARA KELLEN</p>
      <p class="staff-role">Director</p>
      <ul class="contact-list">
        <li><span class="contact-label">M</span><span>0452 987 654</span></li>
        <li><span class="contact-label">E</span><span>mara.kellen@velquora.com</span></li>
      </ul>
    </div>

    <div class="brand brand-front">
      <span class="brand-mark"></span>
      <div class="brand-text">
        <span class="brand-name">Velquora</span>
        <span class="brand-tagline">CLOUD MANAGED SERVICES</span>
      </div>
    </div>

    <div class="company-info">
      <p class="web">www.<strong>velquora</strong>.com</p>
      <p>Suite 5, 48 Marlowe Lane</p>
      <p>Sydney NSW 2000</p>
    </div>
  </section>

  <section class="card card-back" aria-label="Card back">
    <div class="back-band-red"></div>
    <div class="back-band-grey"></div>
    <div class="back-edge"></div>
    <div class="brand brand-back">
      <span class="brand-mark"></span>
      <div class="brand-text">
        <span class="brand-name">Velquora</span>
        <span class="brand-tagline">CLOUD MANAGED SERVICES</span>
      </div>
    </div>
  </section>
</body>
</html>
```